Brightwell Polar Systems Inc.
Business Card, Letter Head, Fax Cover, evelope and T-shirt
Bright & Fun-filled
Dorian Kestle
342 Harrowgate Ave
Harlow Falls, NY, 10999
dkestle@bpsyst.example
www.Bpsyst.example
ill be using a clear plastic card, but also lets have the background as black.
Heating
Air Condition
Ventilation
Duct Work
Refrigeration
Solar, Geothermal
Design, Fabrication & Installation
Sales, Service & Repair

```html
<!DOCTYPE html>
<html lang="en">
<head>
<meta charset="utf-8">
<title>Brightwell Polar Systems Inc. — Business Card</title>
<link href="https://fonts.googleapis.com/css2?family=PT+Serif:ital,wght@0,400;0,700;1,700&display=swap" rel="stylesheet">
<style>
  :root {
    --stage: #ece7df;
    --card: #ecd8bb;
    --card-edge: #d9bf9a;
    --band-dark: #2f8a12;
    --band-light: #8fd23a;
    --band-rule: #c98a22;
    --brand: #3a8a1f;
    --ink: #3b2f22;
    --name: #ffffff;
    --icon: #3f9a1a;
  }
  * { box-sizing: border-box; margin: 0; padding: 0; }
  html, body { width: 1200px; height: 965px; overflow: hidden; }
  body {
    background: var(--stage);
    font-family: "PT Serif", Georgia, serif;
    position: relative;
  }
  .card {
    position: absolute;
    left: 150px; top: 225px;
    width: 900px; height: 514px;
    background: linear-gradient(160deg, #f2e1c6 0%, var(--card) 55%, #e3cba8 100%);
    border: 2px solid var(--card-edge);
    border-radius: 30px;
    box-shadow: 0 14px 34px rgba(0,0,0,.18);
    overflow: hidden;
  }
  .band {
    position: absolute;
    left: 0; top: 40px;
    width: 100%; height: 98px;
    background: linear-gradient(90deg, var(--band-dark) 0%, #4ca51d 30%, var(--band-light) 60%, #4ea51e 85%, var(--band-dark) 100%);
    border-top: 5px solid var(--band-rule);
    border-bottom: 5px solid var(--band-rule);
  }
  .holder-name {
    position: absolute;
    right: 70px; top: 70px;
    color: var(--name);
    font-weight: 700;
    font-style: italic;
    font-size: 32px;
    line-height: 1;
  }
  .brand-name {
    position: absolute;
    left: 46px; top: 222px;
    color: var(--brand);
    font-weight: 700;
    font-size: 40px;
    line-height: 1;
    white-space: nowrap;
  }
  .contact {
    position: absolute;
    left: 46px; top: 348px;
    color: var(--ink);
    font-size: 24px;
    line-height: 1;
  }
  .contact p { margin-bottom: 17px; white-space: nowrap; }
  .phones span { margin-right: 16px; }
  .phones svg { width: 20px; height: 20px; vertical-align: -3px; margin-right: 5px; fill: var(--icon); }
  .web { margin-left: 30px; }
</style>
</head>
<body>
  <div class="card">
    <div class="band"></div>
    <div class="holder-name">Dorian Kestle</div>
    <div class="brand-name">Brightwell Polar Systems Inc.</div>
    <div class="contact">
      <p class="address">342 Harrowgate Ave&nbsp;&nbsp;Harlow Falls, NY, 10999</p>
      <p class="phones">
        <span><svg viewBox="0 0 24 24" aria-hidden="true"><path d="M6.6 10.8a15.1 15.1 0 0 0 6.6 6.6l2.2-2.2c.3-.3.7-.4 1-.2 1.1.4 2.3.6 3.6.6.6 0 1 .4 1 1V20c0 .6-.4 1-1 1A17 17 0 0 1 3 4c0-.6.4-1 1-1h3.5c.6 0 1 .4 1 1 0 1.3.2 2.5.6 3.6.1.3 0 .7-.2 1z"/></svg>718-555-0142</span>
        <span><svg viewBox="0 0 24 24" aria-hidden="true"><path d="M7 1h10a2 2 0 0 1 2 2v18a2 2 0 0 1-2 2H7a2 2 0 0 1-2-2V3a2 2 0 0 1 2-2zm0 4v13h10V5zm5 14.5a1.2 1.2 0 1 0 0 2.4 1.2 1.2 0 0 0 0-2.4z"/></svg>646-555-0187</span>
        <span><svg viewBox="0 0 24 24" aria-hidden="true"><path d="M7 2h8l3 3v5H7zM4 11h16a2 2 0 0 1 2 2v8H2v-8a2 2 0 0 1 2-2zm2 4v2h4v-2z"/></svg>718-555-0163</span>
      </p>
      <p class="online">dkestle@bpsyst.example<span class="web">www.Bpsyst.example</span></p>
    </div>
  </div>
</body>
</html>
```